eBook Cover Design for Healthy Recipes + recipe page

1. I am seeking a cover design for my ebook that contains healthy protein recipes plus I am seeking a design to display recipes in a visually attractive manner. Please refer to the attached images attached for inspo. The a4 cover design that I have done up needs to be enhanced so that the ebook looks really good and visually smoking hot! Please ensure you can provide a full editable working version of the file as the title may change so I need to be able to edit the file.

Brand: Copper Falcon
Book name: 18 Lean Balanced Muscle Meal Ideas

2. I am also seeking the design of an A4 recipe page see image attached as example.

Target Market(s)

Males and females that want to get in shape and want to find healthier options and ideas to make protein recipes.

Industry/Entity Type

Health And Wellness

Font styles to use
Other font styles liked:
• REFER TO IMAGES

Colors
f37122
f68e4e
f9ba93
fac994
faa54b
f78f20
fbc994
fbe7d2
fee3d5

Requirements
Must have
• Cover must contain logo and visually appealing, classy looking design. Must include title.

```html
<!DOCTYPE html>
<html lang="en">
<head>
<meta charset="utf-8">
<title>18 Lean Balanced Muscle Meal Ideas — Copper Falcon</title>
<link href="https://fonts.googleapis.com/css2?family=Barlow+Condensed:wght@600&family=Montserrat:wght@300;400;700&display=swap" rel="stylesheet">
<style>
  :root {
    --ink: #222222;
    --paper: #ffffff;
    --panel-veil: rgba(255, 255, 255, 0.58);
    --copper: #f37122;
    --copper-soft: #f78f20;
  }
  html, body { margin: 0; padding: 0; overflow: hidden; background: var(--paper); }
  .cover {
    position: relative;
    width: 849px;
    height: 1200px;
    overflow: hidden;
    background: var(--paper);
    font-family: "Montserrat", sans-serif;
    color: var(--ink);
  }
  .photo-grid { position: absolute; left: 0; top: 0; width: 849px; height: 1092px; }
  .photo { position: absolute; }
  .col-a { left: 0; width: 278px; }
  .col-b { left: 278px; width: 285px; }
  .col-c { left: 563px; width: 286px; }
  .row-1 { top: 0; height: 224px; }
  .row-2 { top: 224px; height: 288px; }
  .row-3 { top: 512px; height: 288px; }
  .row-4 { top: 800px; height: 292px; }

  .photo-kale { background: radial-gradient(circle at 40% 35%, #6f8f3a, #4d6a2a 55%, #8a5a34 90%); }
  .photo-tea { background: linear-gradient(160deg, #8a6b3a, #c9b27a 50%, #e6dcc4); }
  .photo-pasta { background: radial-gradient(circle at 55% 40%, #e8b25a, #d99066 45%, #f1ece2 80%); }
  .photo-rolls { background: linear-gradient(150deg, #3a2d25, #a48466 45%, #d8c2a4 70%, #4a6b3a); }
  .photo-pancakes { background: linear-gradient(170deg, #e9e4de, #8a5e44 55%, #6a4634); }
  .photo-grapefruit { background: linear-gradient(165deg, #f4e6da, #efc6b6 45%, #d8574a 80%, #3a3a3c); }
  .photo-smoothie { background: radial-gradient(circle at 55% 50%, #f0c79a, #e2a878 40%, #2e2a28 80%); }
  .photo-cookies { background: radial-gradient(circle at 50% 45%, #7a5a44, #a8896e 55%, #ddd4c8); }
  .photo-citrus-drink { background: linear-gradient(160deg, #e8ecf0, #f0a13a 45%, #3a4a8a 75%, #c2d0e2); }
  .photo-watermelon { background: linear-gradient(160deg, #a7c39a, #d83a3a 40%, #e2595a 65%, #5a4030); }
  .photo-spinach-crepe { background: radial-gradient(circle at 50% 45%, #f07a4a 8%, #6a7a3a 25%, #7a8a48 48%, #c9a27a 75%); }
  .photo-plain-crepe { background: radial-gradient(circle at 55% 45%, #c8a870, #d8c7a2 50%, #e6e6ea 75%, #2a2a30); }

  .title-panel {
    position: absolute;
    left: 150px; top: 102px;
    width: 548px; height: 814px;
    box-sizing: border-box;
    background: var(--panel-veil);
    border: 2px solid var(--paper);
  }
  .title-line {
    position: absolute;
    left: 0; width: 849px;
    margin: 0;
    text-align: center;
    line-height: 1;
    white-space: nowrap;
    color: var(--ink);
  }
  .title-number {
    top: 26px;
    font-family: "Barlow Condensed", sans-serif;
    font-weight: 600;
    font-size: 540px;
    letter-spacing: -0.02em;
  }
  .title-light { font-weight: 300; font-size: 62px; letter-spacing: -0.01em; }
  .title-lean { top: 535px; }
  .title-balanced { top: 619px; }
  .title-muscle { top: 696px; font-weight: 700; font-size: 112px; letter-spacing: -0.01em; }
  .title-ideas { top: 823px; }

  .brand-footer {
    position: absolute;
    left: 0; top: 1092px;
    width: 849px; height: 108px;
    display: flex; flex-direction: column; align-items: center; justify-content: center;
  }
  .brand-row { display: flex; align-items: center; gap: 10px; }
  .brand-mark { width: 10px; height: 10px; background: var(--copper); }
  .brand-name {
    font-weight: 400; font-size: 14px; letter-spacing: 0.38em;
    text-transform: uppercase; color: var(--ink);
  }
  .brand-byline {
    margin-top: 4px;
    font-weight: 400; font-size: 7.5px; letter-spacing: 0.42em;
    text-transform: uppercase; color: var(--ink);
  }
</style>
</head>
<body>
<main class="cover">
  <div class="photo-grid">
    <div class="photo col-a row-1 photo-kale" role="img" aria-label="Photo of fresh kale leaves in a wooden bowl"></div>
    <div class="photo col-b row-1 photo-tea" role="img" aria-label="Photo of herbal tea glasses with dill"></div>
    <div class="photo col-c row-1 photo-pasta" role="img" aria-label="Photo of a pasta dish with salmon, parmesan shavings and basil"></div>
    <div class="photo col-a row-2 photo-rolls" role="img" aria-label="Photo of rolled cinnamon protein crepes with blueberries and mint"></div>
    <div class="photo col-b row-2 photo-pancakes" role="img" aria-label="Photo of protein pancakes with blueberries and a strawberry"></div>
    <div class="photo col-c row-2 photo-grapefruit" role="img" aria-label="Photo of a pink grapefruit drink with mint"></div>
    <div class="photo col-a row-3 photo-smoothie" role="img" aria-label="Photo of a peach smoothie with a striped straw"></div>
    <div class="photo col-b row-3 photo-cookies" role="img" aria-label="Photo of oat protein cookies"></div>
    <div class="photo col-c row-3 photo-citrus-drink" role="img" aria-label="Photo of infused water with orange slices and blueberries"></div>
    <div class="photo col-a row-4 photo-watermelon" role="img" aria-label="Photo of a watermelon drink with mint and watermelon wedges"></div>
    <div class="photo col-b row-4 photo-spinach-crepe" role="img" aria-label="Photo of a spinach crepe topped with smoked salmon and basil"></div>
    <div class="photo col-c row-4 photo-plain-crepe" role="img" aria-label="Photo of a thin crepe on a patterned plate"></div>
  </div>

  <div class="title-panel"></div>
  <h1 class="book-title">
    <span class="title-line title-number">18</span>
    <span class="title-line title-light title-lean">LEAN</span>
    <span class="title-line title-light title-balanced">BALANCED</span>
    <span class="title-line title-muscle">MUSCLE</span>
    <span class="title-line title-light title-ideas">MEAL IDEAS</span>
  </h1>

  <footer class="brand-footer">
    <div class="brand-row">
      <span class="brand-mark"></span>
      <span class="brand-name">Copper Falcon</span>
    </div>
    <div class="brand-byline">by Lena Marsh</div>
  </footer>
</main>
</body>
</html>
```